Simple elegant feminine design - Going out on my own as a Mortgage Broker.
My thoughts are the following details on the Front, middle of the card possibly? Phone and email smaller font than my name?
Marnie Veltrin
Finance Specialist
p: 0438 215 962
e: marnie@veltrinlending.com.au
Bottom of the card
residential / commercial / equipment
I would like the Font in Rose Gold maybe white or black background? or Possibly a stone grey - are you able to do a few options? I'd like them embossed
Then I had an idea as a simple logo as per the attached if you get the idea in my scribble, my initials, capital M attached to a small v that leads/follows into a circle? Thicker Font In Rose Gold, middle of the card at the back.
Very open to ideas though and what colour you think would look better with the Rose Gold.
Thanks so much for your help, I am not very creative and savvy with this stuff :-)
Industry/Entity Type
Finance
Contact Information for Business Card
Marnie Veltrin
p: 0438 215 962
Look and feel

```html
<!DOCTYPE html>
<html lang="en">
<head>
<meta charset="utf-8">
<title>Marnie's Business Cards</title>
<link rel="stylesheet" href="https://fonts.googleapis.com/css2?family=Source+Serif+4:opsz,wght@8..60,400;8..60,700&display=swap">
<style>
  :root {
    --page: #ffffff;
    --card: #2e2e2e;
    --rose-gold: #d9978f;
    --card-w: 746px;
    --card-h: 433px;
  }
  * { margin: 0; padding: 0; box-sizing: border-box; }
  html, body {
    width: 1200px;
    height: 1200px;
    overflow: hidden;
    background: var(--page);
  }
  .canvas {
    position: relative;
    width: 1200px;
    height: 1200px;
    font-family: "Source Serif 4", Georgia, serif;
    color: var(--rose-gold);
  }
  .card {
    position: absolute;
    left: 226px;
    width: var(--card-w);
    height: var(--card-h);
    background: var(--card);
  }
  .card--front { top: 129px; }
  .card--back { top: 624px; }

  .brand-mark {
    position: absolute;
    left: 50%;
    transform: translate(-50%, -50%);
    border: 3px solid var(--rose-gold);
    border-radius: 50%;
    display: flex;
    align-items: center;
    justify-content: center;
    text-align: center;
    font-weight: 700;
    line-height: 1.15;
  }
  .card--front .brand-mark {
    top: 216px;
    width: 232px;
    height: 232px;
    border-width: 6px;
    font-size: 30px;
  }
  .card--back .brand-mark {
    top: 80px;
    width: 104px;
    height: 104px;
    font-size: 14px;
  }

  .details {
    position: absolute;
    left: 0;
    width: 100%;
    text-align: center;
  }
  .holder-name {
    top: 176px;
    font-size: 32px;
    font-weight: 700;
    letter-spacing: 0.5px;
  }
  .holder-role {
    top: 216px;
    font-size: 20px;
    font-weight: 700;
  }
  .contact {
    top: 296px;
    font-size: 21px;
    font-weight: 400;
    line-height: 29px;
  }
  .services {
    top: 367px;
    font-size: 24px;
    font-weight: 700;
  }
</style>
</head>
<body>
  <main class="canvas">
    <section class="card card--front" aria-label="Card front">
      <div class="brand-mark">Veltrin<br>Lending</div>
    </section>

    <section class="card card--back" aria-label="Card back">
      <div class="brand-mark">Veltrin<br>Lending</div>
      <h1 class="details holder-name">MARNIE VELTRIN</h1>
      <p class="details holder-role">Finance Specialist</p>
      <p class="details contact">
        phone: 0438 215 962<br>
        email: marnie@veltrinlending.com.au
      </p>
      <p class="details services">residential / commercial / equipment</p>
    </section>
  </main>
</body>
</html>
```